Business card for hedge fund
Vornelle Capital Management
Project: Business card for hedge fund
Business card for hedge fund - Financial Services
Creative Brief
Professional
Wanrudee Halvorsen
Chief Operating Officer
wanru.halvorsen@vornellecap.example
2 additional names: Martin Gaskell, Portfolio Manager p: +1-555-382-4719 e-mail: martin.gaskell@vornellecap.example Jia Luo, Portfolio Manager p: +852-5123-9046 e: jia.luo@vornellecap.example No address to be included

```html
<!DOCTYPE html>
<html lang="en">
<head>
<meta charset="utf-8">
<title>Vornelle Capital Management – Business Card</title>
<link rel="stylesheet" href="https://fonts.googleapis.com/css2?family=Open+Sans:wght@400;600&display=swap">
<style>
  :root {
    --backdrop: #e9e7e4;
    --card-white: #ffffff;
    --card-top-tint: #f4f4f4;
    --band-dark: #3f4042;
    --band-mid: #55575a;
    --ink-dark: #3a3a3a;
    --ink-light: #f2f2f2;
    --ink-muted: #c9c9c9;
    --accent: #f7a21b;
    --icon-disc: #ededed;
    --icon-glyph: #45474a;
  }
  * { margin: 0; padding: 0; box-sizing: border-box; }
  html, body {
    width: 1200px; height: 900px; overflow: hidden;
    background: var(--backdrop);
    font-family: "Open Sans", Arial, sans-serif;
  }
  .canvas {
    position: relative; width: 1200px; height: 900px;
    display: flex; align-items: center; justify-content: center;
  }
  .card {
    position: relative; width: 1000px; height: 572px;
    background: linear-gradient(180deg, var(--card-white) 0%, var(--card-top-tint) 40%);
    box-shadow: 0 10px 30px rgba(0,0,0,0.18);
    overflow: hidden;
  }
  .brand {
    position: absolute; left: 70px; top: 120px;
    color: var(--ink-dark); font-weight: 400; text-transform: uppercase;
  }
  .brand-name { font-size: 64px; letter-spacing: 6px; line-height: 1; }
  .brand-sub { font-size: 21px; letter-spacing: 4.5px; margin-top: 8px; padding-left: 4px; }
  .info-band {
    position: absolute; left: 0; right: 0; top: 236px; bottom: 0;
    background: linear-gradient(160deg, var(--band-mid) 0%, var(--band-dark) 70%);
  }
  .person {
    position: absolute; left: 28px; top: 150px;
    padding-left: 22px; border-left: 8px solid var(--accent);
    color: var(--ink-light);
  }
  .person-name { font-size: 22px; font-weight: 600; line-height: 1.5; }
  .person-title { font-size: 17px; color: var(--ink-muted); line-height: 1.6; }
  .contact-list {
    position: absolute; left: 580px; top: 22px; list-style: none;
  }
  .contact-item {
    display: flex; align-items: center; gap: 14px;
    height: 38px; color: var(--ink-light); font-size: 17px;
  }
  .contact-icon { width: 24px; height: 24px; flex: none; }
</style>
</head>
<body>
<main class="canvas">
  <article class="card">
    <header class="brand">
      <div class="brand-name">Vornelle</div>
      <div class="brand-sub">Capital Management</div>
    </header>

    <section class="info-band">
      <div class="person">
        <div class="person-name">Wanrudee Halvorsen</div>
        <div class="person-title">Chief Operating Officer</div>
      </div>

      <ul class="contact-list">
        <li class="contact-item">
          <svg class="contact-icon" viewBox="0 0 24 24" aria-hidden="true">
            <circle cx="12" cy="12" r="12" fill="var(--icon-disc)"/>
            <path d="M8.5 6.5l2 2.5-1.2 1.4c.8 1.7 2 2.9 3.7 3.7l1.4-1.2 2.5 2-1.3 2c-4.2-.2-8.2-4.2-8.4-8.4z" fill="var(--icon-glyph)"/>
          </svg>
          <span>+1-555-204-7716</span>
        </li>
        <li class="contact-item">
          <svg class="contact-icon" viewBox="0 0 24 24" aria-hidden="true">
            <circle cx="12" cy="12" r="12" fill="var(--icon-disc)"/>
            <rect x="8.5" y="5.5" width="7" height="13" rx="1.2" fill="var(--icon-glyph)"/>
            <rect x="9.7" y="7" width="4.6" height="8.2" fill="var(--icon-disc)"/>
            <circle cx="12" cy="16.8" r="0.8" fill="var(--icon-disc)"/>
          </svg>
          <span>+1-555-318-9042</span>
        </li>
        <li class="contact-item">
          <svg class="contact-icon" viewBox="0 0 24 24" aria-hidden="true">
            <circle cx="12" cy="12" r="12" fill="var(--icon-disc)"/>
            <rect x="6" y="10" width="12" height="8" rx="1" fill="var(--icon-glyph)"/>
            <path d="M7 10c0-3 10-3 10 0" fill="none" stroke="var(--icon-glyph)" stroke-width="2"/>
            <rect x="9" y="12" width="6" height="2" fill="var(--icon-disc)"/>
          </svg>
          <span>+1-555-671-2280</span>
        </li>
        <li class="contact-item">
          <svg class="contact-icon" viewBox="0 0 24 24" aria-hidden="true">
            <circle cx="12" cy="12" r="12" fill="var(--icon-disc)"/>
            <rect x="6" y="8" width="12" height="8.5" rx="1" fill="var(--icon-glyph)"/>
            <path d="M6.5 8.6l5.5 4.3 5.5-4.3" fill="none" stroke="var(--icon-disc)" stroke-width="1.2"/>
          </svg>
          <span>wanru.halvorsen@vornellecap.example</span>
        </li>
        <li class="contact-item">
          <svg class="contact-icon" viewBox="0 0 24 24" aria-hidden="true">
            <circle cx="12" cy="12" r="12" fill="var(--icon-disc)"/>
            <g fill="none" stroke="var(--icon-glyph)" stroke-width="1.4">
              <circle cx="12" cy="12" r="6"/>
              <ellipse cx="12" cy="12" rx="2.6" ry="6"/>
              <line x1="6" y1="12" x2="18" y2="12"/>
            </g>
          </svg>
          <span>www.vornellecap.example</span>
        </li>
      </ul>
    </section>
  </article>
</main>
</body>
</html>
```